E Newsletter Design

A very strong ENewsletter.. we are a recruitment agency and each fortnight we send out a "hot jobs" newsletter to our candidates, and a "hot Candidates" to our clients.

Hot Jobs: a list of about 8 jobs which are our"hottest" jobs and try to sell some great points about the jobs to attract the candidate to apply for the job.

Hot Candidates: "a list of about 8 candidates which are "hottest" candidates and we need to try to sell these candidates to our clients, and get them to call us about them.

Both of these newsletter will be to attract a professional type of person... we are working in the mining & resources industry, so these candidates and jobs are not easy to find.

We have an example of one that we have been using, I am happy for the headlines to be reworded as well.

The final product will be 2 HTML files one for hot jobs and other for hot candidates. We will need original psd files as well.

Target Market(s)

mid level positions to senior level positions ... mostly men for the hot jobs, and mixed men and woman for the hot candidates

Industry/Entity Type

Mining

Requirements
Must have
• Strong headlines... less images and more about good headlines in strong colours.. must be similar style and colours as per our website. www.staffquarry7.com

Good strong headline, using a black background, with our logo.. and keep it bright.

```html
<!DOCTYPE html>
<html lang="en">
<head>
<meta charset="utf-8">
<title>Kestrel Staffing – Hot Jobs</title>
<link rel="stylesheet" href="https://fonts.googleapis.com/css2?family=Arimo:ital,wght@0,400;0,700;1,400&family=Oswald:wght@500;600&display=swap">
<style>
:root{
  --page:#e3e6eb;
  --card:#ffffff;
  --ink:#4a4a4a;
  --olive-dark:#4f4614;
  --olive-text:#6b5e10;
  --olive:#99924f;
  --olive-light:#b8b070;
  --icon:#5a5222;
  --gold:#b9a560;
  --white:#ffffff;
}
*{margin:0;padding:0;box-sizing:border-box}
html,body{width:800px;height:1200px;overflow:hidden;background:var(--page)}
body{position:relative;font-family:"Arimo",Helvetica,Arial,sans-serif;color:var(--ink)}
.topbar{position:absolute;top:19px;left:100px;width:600px;height:20px;font-size:11px;color:#111}
.topbar .issue-date{position:absolute;left:0;top:0;font-size:14px}
.topbar .utility-links{position:absolute;right:0;top:3px;display:flex;gap:16px}
.newsletter{position:absolute;left:100px;top:60px;width:600px;height:846px;background:var(--card);border-radius:5px;box-shadow:0 1px 4px rgba(0,0,0,.35);overflow:hidden}
.masthead{height:135px;background:linear-gradient(#2a2a2a,#050505);display:flex;align-items:center;justify-content:center;gap:14px}
.brand-mark{width:34px;height:34px;border-radius:50%;background:var(--gold)}
.brand-name{font-family:"Oswald",Impact,sans-serif;font-weight:600;font-size:40px;letter-spacing:1px;color:var(--white);text-transform:uppercase}
.hot-band{height:80px;background:linear-gradient(90deg,var(--olive),var(--olive-light) 50%,var(--olive));text-align:center;font-family:"Oswald",Impact,sans-serif;font-weight:600;text-transform:uppercase;padding-top:12px}
.hot-band .headline{color:var(--white);font-size:21px;line-height:26px;letter-spacing:.5px}
.hot-band .sector{color:#111;font-size:18px;line-height:24px;letter-spacing:.5px}
.intro{margin:0 15px;padding-top:17px;height:85px;border-bottom:1px solid var(--olive-dark);text-align:center;color:var(--olive-text);font-size:14px;line-height:17px}
.job{padding:0 15px}
.job-title{margin-top:17px;font-size:18px;font-weight:400;color:var(--olive-dark)}
.highlights{list-style:none;margin-top:10px;padding-left:22px}
.highlights li{position:relative;padding-left:16px;font-style:italic;font-size:14px;line-height:18px;color:#444}
.highlights li::before{content:"";position:absolute;left:0;top:5px;border-left:7px solid #555;border-top:4px solid transparent;border-bottom:4px solid transparent}
.job-summary{margin-top:14px;font-size:14px;line-height:17px;text-align:justify;hyphens:auto;-webkit-hyphens:auto}
.skills-title{margin-top:17px;font-size:14px;font-weight:700}
.skills{margin-top:13px;font-size:14px;line-height:17px;list-style:none;hyphens:auto;-webkit-hyphens:auto}
.apply{margin-top:22px}
.apply-row{display:flex;align-items:center;height:32px;margin-bottom:3px;font-size:14px}
.apply-icon{width:32px;height:32px;border-radius:50%;background:var(--icon);display:flex;align-items:center;justify-content:center;margin-right:14px}
.apply-row strong{margin-left:5px;color:#333}
.footer{position:absolute;left:0;bottom:0;width:600px;height:71px;background:linear-gradient(#1e1e1e,#050505);display:flex;align-items:center;padding:0 15px}
.footer .brand-mark{width:26px;height:26px}
.footer .brand-name{font-size:30px;margin-left:10px}
.social{margin-left:auto;display:flex;gap:18px}
.social span{width:30px;height:30px;border-radius:4px;display:block}
.social .s1{background:#1d7fb8}.social .s2{background:#55b9e6}.social .s3{background:#3b5a9a}
.copyright{position:absolute;top:915px;left:0;width:800px;text-align:center;font-size:11px;color:#111}
</style>
</head>
<body>
<header class="topbar">
  <span class="issue-date">April 2012</span>
  <nav class="utility-links"><span>Unsubscribe</span><span>|</span><span>Help</span><span>|</span><span>Contact Us</span></nav>
</header>

<main class="newsletter">
  <div class="masthead">
    <span class="brand-mark"></span><span class="brand-name">Kestrel Staffing</span>
  </div>
  <div class="hot-band">
    <div class="headline">Check out this weeks “Hot Jobs”</div>
    <div class="sector">Construction &amp; Mining</div>
  </div>
  <p class="intro">Keep your finger on the pulse! Each fortnight we will send you our "hottest jobs". Whether you are looking now, or in the future (or you might know someone who is looking) have a look below and know what is going on in your market.</p>

  <article class="job">
    <h2 class="job-title">CHPP Electrical Maintenance Planner - QLD &amp; NW NSW</h2>
    <ul class="highlights">
      <li>Multi national mining stronghold. 2 roles. Electrical trade Q 2yrs CHPP</li>
      <li>M-F site based, Qld &amp; NW NSW</li>
      <li>Base super RELOCATION housing subsidy annual bonus!!</li>
    </ul>
    <p class="job-summary">We represent a multi national client operating a leading coal producing facility in the North West NSW and Central Qld mining regions seeking two Electrical Trade qualified candidates with CHPP or processing environment experience. As Electrical Maintenance Planner you will take charge of effective planning and scheduling of weekly Electrical Maintenance activities across the CHPP site.</p>
    <h3 class="skills-title">CHPP Electrical Maintenance Planner skills required:</h3>
    <ul class="skills">
      <li>- Electrical trade qualifications.</li>
      <li>- 2+yrs exp similar role, CHPP/processing environment.</li>
      <li>- Exp planning &amp; scheduling of weekly Electrical maintenance activities, heavy industry.</li>
      <li>- Proficient computer skills &amp; exp computer based maintenance systems - (Valdris/Tallyo/similar).</li>
      <li>- Exceptional communicator, proven people management skills &amp; relationship develop-<br>ment.</li>
    </ul>
    <div class="apply">
      <div class="apply-row">
        <span class="apply-icon"><svg width="16" height="12" viewBox="0 0 16 12"><rect x="0.5" y="0.5" width="15" height="11" fill="#fff"/><path d="M1 1l7 6 7-6" fill="none" stroke="#5a5222" stroke-width="1.4"/></svg></span>
        Email us your CV to: <strong>jobs@staffquarry7.com</strong>
      </div>
      <div class="apply-row">
        <span class="apply-icon"><svg width="16" height="16" viewBox="0 0 16 16" fill="none" stroke="#fff" stroke-width="2"><rect x="1.5" y="7" width="7" height="4.5" rx="2.2" transform="rotate(-45 5 9.3)"/><rect x="7.5" y="4.5" width="7" height="4.5" rx="2.2" transform="rotate(-45 11 6.7)"/></svg></span>
        Or Apply online at: <strong>www.staffquarry7.com</strong>
      </div>
    </div>
  </article>

  <footer class="footer">
    <span class="brand-mark"></span><span class="brand-name">Kestrel Staffing</span>
    <div class="social"><span class="s1" role="img" aria-label="Professional network link"></span><span class="s2" role="img" aria-label="Microblog link"></span><span class="s3" role="img" aria-label="Social network link"></span></div>
  </footer>
</main>

<p class="copyright">2012 Kestrel Staffing All right reserved</p>
</body>
</html>
```